New Year's Eve Wedding Save the Date

Mira and Kevin (we) are getting married 2016-12-31. I'm a hockey player, and she's into movies... we have 2 yellow labs, and we want a Save the Date postcard that matches our personality and the excitement of the event. See attached mock up that I've created (which will be what we fall back on if we can't find a design we like). I like the idea of the silhouette people and dogs under fireworks but am open to other concepts as well. String lights, champagne bottles/flutes, etc...

Industry/Entity Type

Wedding

Font styles to use
Script

```html
<!DOCTYPE html>
<html lang="en">
<head>
<meta charset="utf-8">
<title>Save the Date – Kevin &amp; Mira</title>
<link rel="stylesheet" href="https://fonts.googleapis.com/css2?family=Pinyon+Script&family=Bodoni+Moda:ital,wght@1,400&display=swap">
<style>
  :root {
    --cream: #fbf8f1;
    --ivory: #f3ecdd;
    --champagne: #e6cf9f;
    --gold-deep: #d4ad63;
    --ink: #1f2521;
    --shadow-gold: #c9b27e;
    --glitter-light: #efe49a;
    --glitter-mid: #d8c85c;
    --glitter-dark: #b9a43e;
  }
  html, body {
    margin: 0;
    padding: 0;
    width: 1200px;
    height: 930px;
    overflow: hidden;
  }
  .postcard {
    position: relative;
    width: 1200px;
    height: 930px;
    overflow: hidden;
    background:
      radial-gradient(circle at 92% 12%, rgba(212,173,99,0.75) 0, rgba(230,207,159,0.45) 14%, rgba(251,248,241,0) 34%),
      radial-gradient(circle at 3% 98%, rgba(230,207,159,0.6) 0, rgba(251,248,241,0) 22%),
      radial-gradient(circle at 97% 95%, rgba(230,207,159,0.45) 0, rgba(251,248,241,0) 20%),
      radial-gradient(circle at 40% 50%, var(--cream) 0, var(--ivory) 80%);
  }
  .bokeh {
    position: absolute;
    border-radius: 50%;
    border: 2px solid rgba(255,255,255,0.55);
    background: rgba(255,255,255,0.18);
  }
  .headline {
    position: absolute;
    left: 0;
    right: 0;
    top: 148px;
    margin: 0;
    text-align: center;
    font-family: "Pinyon Script", cursive;
    font-weight: 400;
    font-size: 168px;
    line-height: 1;
    color: var(--ink);
    text-shadow: 6px 4px 0 var(--shadow-gold);
    letter-spacing: 1px;
  }
  .details {
    position: absolute;
    left: 0;
    right: 0;
    top: 378px;
    text-align: center;
    font-family: "Bodoni Moda", serif;
    font-style: italic;
    font-weight: 400;
    color: var(--ink);
  }
  .couple, .wedding-date {
    margin: 0;
    font-size: 78px;
    line-height: 98px;
  }
  .couple { letter-spacing: 2px; }
  .silhouette-art {
    position: absolute;
    left: 400px;
    top: 596px;
    width: 400px;
    height: 308px;
    border-radius: 6px;
    background: linear-gradient(160deg, var(--glitter-light), var(--glitter-mid) 55%, var(--glitter-dark));
    box-shadow: 3px 4px 6px rgba(120,110,60,0.35);
  }
</style>
</head>
<body>
  <main class="postcard">
    <span class="bokeh" style="left:30px;top:20px;width:180px;height:180px"></span>
    <span class="bokeh" style="left:290px;top:100px;width:220px;height:220px"></span>
    <span class="bokeh" style="left:960px;top:100px;width:70px;height:70px"></span>
    <span class="bokeh" style="left:1130px;top:120px;width:50px;height:50px"></span>
    <span class="bokeh" style="left:40px;top:350px;width:230px;height:230px"></span>
    <span class="bokeh" style="left:870px;top:560px;width:220px;height:220px"></span>
    <span class="bokeh" style="left:30px;top:850px;width:60px;height:60px"></span>
    <span class="bokeh" style="left:210px;top:870px;width:50px;height:50px"></span>

    <h1 class="headline">Save the Date</h1>

    <section class="details">
      <p class="couple">Kevin &amp; Mira</p>
      <p class="wedding-date">12.31.2016</p>
    </section>

    <div class="silhouette-art" role="img" aria-label="Gold glitter silhouette of the couple kissing with their two dogs beside them"></div>
  </main>
</body>
</html>
```